Boutique Recruiting Firm Needs Eye-Catching Business Cards (and potentially new logo)!

I run a recruiting company in Charleston, South Carolina. I have a ton of networking events coming up and need business cards to grab potential clients attention.

I currently have a logo but if you want to try and recreate the logo to something more modern I am open to that. If you do decide to create a new logo please submit the business card with the old logo and the new one.

Staffing Beyond the Lantern, LLC is the name of my company. I create videos to my clients and candidates which allows me to standout from my competition so I would like a business card (and possibly new logo) to do the same.

I do not specialize in any one industry of recruiting.

Industry/Entity Type

Business

```html
<!DOCTYPE html>
<html lang="en">
<head>
<meta charset="utf-8">
<title>Staffing Beyond the Lantern, LLC — Business Card</title>
<link rel="stylesheet" href="https://fonts.googleapis.com/css2?family=Questrial&display=swap">
<style>
  :root {
    --paper: #ffffff;
    --ink: #070707;
    --sky: #00a3e0;
    --sand: #d9c7a7;
  }
  html, body {
    margin: 0;
    padding: 0;
    width: 1200px;
    height: 686px;
    overflow: hidden;
    background: var(--paper);
  }
  .card {
    position: relative;
    width: 1200px;
    height: 686px;
    background: var(--paper);
    font-family: "Questrial", sans-serif;
    overflow: hidden;
  }
  .card-shapes {
    position: absolute;
    inset: 0;
    width: 1200px;
    height: 686px;
  }
  .brand-name {
    position: absolute;
    left: 30px;
    top: 232px;
    margin: 0;
    font-size: 56px;
    line-height: 1.12;
    font-weight: 400;
    color: var(--ink);
    letter-spacing: 0.5px;
  }
  .person-name {
    position: absolute;
    left: 740px;
    top: 180px;
    margin: 0;
    font-size: 47px;
    font-weight: 400;
    letter-spacing: 3px;
    color: var(--ink);
    white-space: nowrap;
  }
  .person-role {
    position: absolute;
    left: 887px;
    top: 266px;
    margin: 0;
    font-size: 39px;
    letter-spacing: 2px;
    color: var(--sand);
  }
  .contact {
    position: absolute;
    margin: 0;
    font-size: 34px;
    letter-spacing: 2px;
    color: var(--sand);
    white-space: nowrap;
  }
  .contact-phone { left: 857px; top: 452px; }
  .contact-email { left: 840px; top: 543px; }
  .contact-web   { left: 813px; top: 618px; }
</style>
</head>
<body>
<main class="card">
  <svg class="card-shapes" viewBox="0 0 1050 600" preserveAspectRatio="none" aria-hidden="true">
    <!-- upper corner -->
    <polygon fill="var(--sky)" points="820,0 860,0 795,135 757,135"/>
    <polygon fill="var(--ink)" points="858,0 1050,0 1050,135 793,135"/>
    <!-- lower panel -->
    <polygon fill="var(--sand)" points="588,230 706,230 668,310"/>
    <polygon fill="var(--sky)" points="706,230 742,230 570,600 530,600"/>
    <polygon fill="var(--ink)" points="740,230 1050,230 1050,600 568,600"/>

    <!-- phone icon -->
    <g class="icon-phone">
      <circle cx="710" cy="407" r="30" fill="var(--sand)"/>
      <path fill="var(--ink)" d="M699,392 l6,-2 l5,11 l-4,4 q3,7 10,11 l4,-4 l11,5 l-2,6 q-3,4 -9,3 q-15,-4 -24,-21 q-3,-8 3,-13 z"/>
    </g>
    <!-- envelope icon -->
    <g class="icon-mail">
      <circle cx="681" cy="485" r="30" fill="var(--sand)"/>
      <rect x="667" y="475" width="28" height="20" fill="none" stroke="var(--ink)" stroke-width="2"/>
      <polyline points="667,475 681,487 695,475" fill="none" stroke="var(--ink)" stroke-width="2"/>
    </g>
    <!-- globe icon -->
    <g class="icon-web">
      <circle cx="650" cy="548" r="30" fill="var(--sand)"/>
      <circle cx="650" cy="548" r="20" fill="none" stroke="var(--ink)" stroke-width="2"/>
      <ellipse cx="650" cy="548" rx="9" ry="20" fill="none" stroke="var(--ink)" stroke-width="2"/>
      <line x1="630" y1="548" x2="670" y2="548" stroke="var(--ink)" stroke-width="2"/>
      <polygon fill="var(--sand)" stroke="var(--ink)" stroke-width="2" points="660,556 682,566 672,569 678,580 673,582 667,571 660,578"/>
    </g>
  </svg>

  <h1 class="brand-name">Staffing Beyond<br>the Lantern, LLC</h1>

  <p class="person-name">Lorem Hissup</p>
  <p class="person-role">Manager</p>

  <p class="contact contact-phone">555.555.5555</p>
  <p class="contact contact-email">info@lorem.com</p>
  <p class="contact contact-web">www.lorem.com</p>
</main>
</body>
</html>
```